Coral Voyage Mate - A Travel Services Website

Islestay Cottage Rentals is a company that provides travels services to home owners and travellers to Barbados. Coral Voyage Mate is a particular brand targeting travelling guests with specific set of travel services. The brand slogan is:

'Getting you the best for less'

The travel services will include:

- Coral Voyage Mate Perk Pass
- Car Hire Quote Service
- Mobile Phone Sim Cards
- Prepaid Debit Cards
- Airport Hotel Booking
- Airport Lounge Booking
- Airport Parking

There will also be a travel planner function for guests.

The main puropse of the site is as follows:

1. Registration for the Coral Voyage Mate Perk Pass

2. Creation of user account which the guest will frequently return to check for updates

3. Purchase of ancillary travel products and services

4. To use the Travel Planner

5. To gather data on holiday home owners in Barbados

A site map can be seen at the following link:

http://plotgrid-example.com/charts/viewChart/4kqzvb8ynhpwe2ufa6rj0xmc51tlsg9odiq3ye70bnc8hva2wk

Webpage templates (2 required)

The first will be form control heavy (text boxes, checkboxes ect). It will need failure and success messages / indicators etc.

The second will be a general content area with a secondary navigation area (i.e for sub sections of the current section). This will house text / headings and images.

Both will require header, primary navigation, content and footer areas.

N.B. Please not that I am not technical and the above webtemplate narrative has been supplied by my web developer/programmer. If you have any questions, please ask me any questions and I will get an answer from him.

Target Market(s)

My customers tend to be:

Sex: Female
Age: 24-55
Location: UK, USA, Canada
Social Class: A,B,C1
Income: Medium income bracket

They are possibly visiting Barbados for the first and only time. It is an expensive destination and is accessible to people with a medium to high income. They still desire 'value for money'. Therefore the sight must give guests confidence that Coral Voyage Mate is 'their friend', is seeking to offer the best value deals for their vacation/holiday.

Industry/Entity Type

Travel

Requirements
Must have
• The site templates must be professional, aspirational, trustworthy, reassuring, clean, innovative, fun. When people visit the site they should be excited about the savings that they can make and want to return as there is a perceived benefit for them. It must look expensive and professional in its projected image.
Nice to have
• Smooth currved lines, seperated boxed areas for content, as simple and uncluttered layout and it must be simple to read!
Should not have
• It should not be cartoonly, despite my attached logo and must not look cheap.

```html
<!DOCTYPE html>
<html lang="en">
<head>
<meta charset="utf-8">
<title>Coral Voyage Mate – Account Settings</title>
<link rel="stylesheet" href="https://fonts.googleapis.com/css2?family=Open+Sans:ital,wght@0,400;0,600;0,700;0,800;1,600&display=swap">
<style>
:root{
  --orange:#f18a1c;--orange-dark:#d9640a;--orange-light:#f9b24a;
  --blue:#2ba8e0;--blue-light:#8fd3f2;--red:#e2222d;
  --ink:#1c1c1c;--grey-bg:#f1f1f1;--panel:#ececec;--line:#d6d6d6;--pill:#2b2b2b;
}
*{box-sizing:border-box;margin:0;padding:0}
html,body{width:915px;height:1200px;overflow:hidden}
body{font-family:"Open Sans",Arial,sans-serif;color:var(--ink);background:var(--grey-bg);position:relative;font-size:10px}
.abs{position:absolute}
.brand{left:48px;top:24px;display:flex;align-items:center;gap:10px;font-size:30px;font-weight:800;color:var(--red)}
.brand-dot{width:44px;height:44px;border-radius:50%;background:var(--orange)}
.login-field{top:40px;width:165px;height:21px;border-radius:11px;background:#fff;border:1px solid var(--line);padding:3px 10px;font-size:9px;color:#333}
.forgot{left:711px;top:64px;font-size:8px;text-decoration:underline;color:#333}
.login-btn{left:821px;top:65px;width:46px;height:17px;border-radius:9px;background:linear-gradient(#5cc8f3,#1f93cf);color:#111;font-size:9px;font-weight:600;text-align:center;line-height:17px}
.main-nav{left:47px;top:103px;width:821px;height:26px;border-radius:13px;background:linear-gradient(#f8a040,var(--orange-dark));display:flex;align-items:center;justify-content:space-around;padding:0 18px}
.main-nav span{color:#fff;font-weight:700;font-size:11px}
.main-nav i{width:1px;height:12px;background:rgba(255,255,255,.7)}
.hero{left:47px;top:143px;width:821px;height:261px;border:3px solid var(--blue);border-radius:10px;overflow:hidden;background:linear-gradient(90deg,#2a9fd8 0%,#63c2ea 45%,#cfe9f3 100%)}
.hero-scene{position:absolute;inset:0;background:linear-gradient(180deg,rgba(255,255,255,.15),rgba(20,120,180,.25))}
.hero-text{position:absolute;left:12px;top:18px;color:#fff}
.hero-title{font-size:24px;font-weight:800;color:var(--red);letter-spacing:-.3px}
.hero-slogan{font-size:15px;font-weight:700;color:#ffe14a;margin-top:-2px}
.hero-sub{font-size:17px;font-weight:800;margin-top:10px}
.hero-list{list-style:none;margin-top:2px}
.hero-list li{font-size:13px;font-weight:700;line-height:21.6px}
.hero-list li::before{content:"› ";color:#fff}
.card{position:absolute;border-radius:8px;box-shadow:0 3px 8px rgba(0,0,0,.35)}
.card-a{left:390px;top:22px;width:220px;height:140px;background:linear-gradient(160deg,#7ccff0,#2f9ed6 60%,#f3e7c5);transform:rotate(-14deg)}
.card-b{left:543px;top:92px;width:242px;height:152px;background:linear-gradient(#fff 55%,#9fd4ef)}
.pill{height:20px;border-radius:10px;background:var(--pill);color:#fff;font-weight:700;font-size:11px;padding:0 10px;line-height:20px;display:inline-block}
.side{left:47px;top:424px;width:211px}
.welcome{font-size:9px;font-weight:700;margin:15px 0 10px 17px}
.side-nav{list-style:none;background:#e6e6e6}
.side-nav li{height:26px;line-height:26px;border-bottom:1px solid #fafafa;padding-left:10px;font-size:9px}
.side-nav li::before{content:"›";font-weight:800;margin-right:10px}
.promo{width:211px;border-radius:10px;display:flex;align-items:center;justify-content:center;text-align:center;color:#fff;font-size:25px;font-weight:800;line-height:31px;text-shadow:0 1px 2px rgba(0,0,0,.5)}
.promo-book{height:140px;margin-top:17px;background:linear-gradient(var(--orange-light),var(--orange));border:2px solid #e6861d}
.promo-places{height:136px;margin-top:16px;background:linear-gradient(#6ecbf2,#1f9bd3);border:2px solid #3aaee0}
.content{left:295px;top:424px;width:573px}
.section-label{font-size:9px;font-weight:700;margin-left:13px}
.panel{background:var(--panel);border-radius:8px;position:relative}
.row{position:absolute;left:13px;display:flex;align-items:center;font-size:9px;font-weight:700}
.row label{width:122px}
.input{width:283px;height:18px;border-radius:9px;background:#fff;border:1px solid var(--line)}
.select{position:relative}
.select::after{content:"";position:absolute;right:0;top:0;width:24px;height:100%;border-radius:0 9px 9px 0;background:#6b6b6b}
.select::before{content:"";position:absolute;right:7px;top:6px;border:5px solid transparent;border-top:6px solid #fff;z-index:1}
.mini{width:68px;height:18px;border-radius:9px;background:#fff;border:1px solid var(--line);margin-right:10px;font-size:9px;font-weight:700;padding-left:18px;line-height:16px}
.check{width:10px;height:10px;border:1px solid #777;background:#fff;margin-right:13px}
.btn{position:absolute;top:1040px;height:23px;border-radius:12px;color:#fff;font-weight:700;font-size:11px;text-align:center;line-height:23px}
.btn-submit{left:295px;width:97px;background:linear-gradient(var(--orange-light),var(--orange))}
.btn-reset{left:402px;width:96px;background:#7a7a7a}
.footer{left:0;top:1101px;width:915px;height:99px;background:linear-gradient(var(--orange-light),var(--orange));color:#fff}
.footer-brand{position:absolute;left:52px;top:22px;display:flex;align-items:center;gap:8px;font-size:22px;font-weight:800;color:#5a3a12}
.footer-brand .brand-dot{width:34px;height:34px;background:#fff}
.copy{position:absolute;left:55px;top:80px;font-size:8px;font-weight:700}
.divider{position:absolute;top:0;width:1px;height:99px;background:#c8541a}
.call{position:absolute;left:283px;width:232px;top:22px;text-align:center}
.call h3{font-size:17px;font-weight:700}
.call p{font-size:25px;font-weight:800;margin-top:-2px}
.testi{position:absolute;left:555px;top:12px;width:320px}
.testi h3{font-size:12px;font-weight:700}
.testi p{font-size:9.5px;font-weight:600;font-style:italic;line-height:13px;margin-top:3px}
</style>
</head>
<body>
<header>
  <div class="abs brand"><span class="brand-dot"></span>Coral Voyage Mate</div>
  <div class="abs login-field" style="left:528px">User name</div>
  <div class="abs login-field" style="left:703px">Password</div>
  <div class="abs forgot">Forgot Password?</div>
  <div class="abs login-btn">Log in</div>
</header>

<nav class="abs main-nav">
  <span>Home</span><i></i><span>Airport Parking</span><i></i><span>Airport Hotel</span><i></i><span>Car Hire</span><i></i><span>Attractions</span><i></i><span>Travel Money</span><i></i><span>Mobile Simcards</span><i></i><span>Privilege Card</span>
</nav>

<section class="abs hero">
  <div class="hero-scene" role="img" aria-label="Tropical beach with palm trees and turquoise sea"></div>
  <div class="hero-text">
    <div class="hero-title">Coral Voyage Mate</div>
    <div class="hero-slogan">'Getting you the best for less'</div>
    <div class="hero-sub">TRAVEL SERVICES:</div>
    <ul class="hero-list">
      <li>Coral Voyage Mate Perk Pass</li>
      <li>Car Hire Quote Service</li>
      <li>Mobile Phone Sim Cards</li>
      <li>Prepaid Debit Cards</li>
      <li>Airport Hotel Booking</li>
      <li>Airport Lounge Booking</li>
      <li>Airport Parking</li>
    </ul>
  </div>
  <div class="card card-a" role="img" aria-label="Perk Pass membership card with beach artwork"></div>
  <div class="card card-b" role="img" aria-label="Partner attractions booking card"></div>
</section>

<aside class="abs side">
  <span class="pill">Account Dashboard:</span>
  <p class="welcome">Welcome ! Elliot R. K.</p>
  <ul class="side-nav">
    <li>Home</li><li>Preparation List</li><li>Get a Barbadose Card</li><li>Get Car Here</li><li>Settings</li>
  </ul>
  <div class="promo promo-book" role="img" aria-label="Aeroplane in flight">Book Your<br>Trip Now</div>
  <div class="promo promo-places" role="img" aria-label="Island beach view">Barbados<br>Locations</div>
</aside>

<main class="abs content">
  <span class="pill">Account Settings:</span>
  <p class="section-label" style="margin-top:19px">Your Details:</p>
  <div class="panel" style="margin-top:7px;height:118px">
    <div class="row" style="top:19px"><label>Email Address:</label><span class="input"></span></div>
    <div class="row" style="top:50px"><label>Password:</label><span class="input"></span></div>
    <div class="row" style="top:81px"><label>Confirm Passport</label><span class="input"></span></div>
  </div>
  <p class="section-label" style="margin-top:21px">Personal Details:</p>
  <div class="panel" style="margin-top:9px;height:270px">
    <div class="row" style="top:17px"><label>First Name:</label><span class="input"></span></div>
    <div class="row" style="top:48px"><label>Last Name:</label><span class="input"></span></div>
    <div class="row" style="top:79px"><label>House Number/Street:</label><span class="input"></span></div>
    <div class="row" style="top:111px"><label>Line 2:</label><span class="input"></span></div>
    <div class="row" style="top:142px"><label>Town:</label><span class="input"></span></div>
    <div class="row" style="top:174px"><label>Country:</label><span class="input select"></span></div>
    <div class="row" style="top:205px"><label>Phone:</label><span class="input"></span></div>
    <div class="row" style="top:236px"><label>Departure Date:</label><span class="mini select">Jan</span><span class="mini select">01</span><span class="mini select">2010</span></div>
  </div>
  <p class="section-label" style="margin-top:25px">Account Options:</p>
  <div class="panel" style="margin-top:9px;height:63px">
    <div class="row" style="top:16px"><span class="check"></span>Receive Weekly email updates for your to-do list:</div>
    <div class="row" style="top:37px"><span class="check"></span>Recieve Selected Offers:</div>
  </div>
</main>
<div class="btn btn-submit">Submit</div>
<div class="btn btn-reset">Reset</div>

<footer class="abs footer">
  <div class="footer-brand"><span class="brand-dot"></span>Coral Voyage Mate</div>
  <div class="copy">Copyright © 2010 | All Rights Reserved.</div>
  <span class="divider" style="left:283px"></span>
  <div class="call"><h3>Call Now</h3><p>111 555 209</p></div>
  <span class="divider" style="left:515px"></span>
  <div class="testi">
    <h3>Testimonials:</h3>
    <p>“ Lorem Ipsum is simply dummy text of the printing and typesetting industry. Lorem Ipsum has been the industry's standard dummy text ever since the 1500s, when an unknown printer took a galley of type and scrambled it to make a type specimen book. ”</p>
  </div>
</footer>
</body>
</html>
```